Create a website for a car broker/car buyers advocate

build a website to suit a car brokering/car buying service. The design should communicate saving people time, money and stress by outsourcing the purchasing process for thier new car. I woudl like a modern site which is scroll able all on one page and wouldnt mind a dark or minimalistic theme. i have uploaded the logo which has also been designed by pixel harbor

Target Market(s)

general consumers, new car buyers, car collectors

Industry/Entity Type

Car Dealer

Font styles to use
Sans Serif

Colors

Designer to choose colors to be used in the design.

Requirements
Must have
• single page scrollable site
• modern design
• professional but fun
Nice to have
• some websites i like of similar businesses are :
• http://www.motorvane.com.au/
• https://drivelumen.com.au/

```html
<!DOCTYPE html>
<html lang="en">
<head>
<meta charset="utf-8">
<title>Vantage Brokers</title>
<link rel="stylesheet" href="https://fonts.googleapis.com/css2?family=Poppins:wght@300;400;500;600&display=swap">
<style>
:root{
  --blue:#1096dc;
  --blue-dark:#0b7fc0;
  --ink:#2b2f36;
  --muted:#8a8f98;
  --line:#e3e6ea;
  --soft:#f3f4f7;
  --footer:#3e404b;
  --white:#ffffff;
}
*{box-sizing:border-box;margin:0;padding:0}
html,body{width:1200px;height:3579px;overflow:hidden}
body{font-family:"Poppins",sans-serif;color:var(--ink);background:var(--white);position:relative}
.abs{position:absolute}
.btn{position:absolute;display:flex;align-items:center;justify-content:center;background:var(--blue);color:var(--white);border-radius:22px;font-size:13px;font-weight:500;white-space:nowrap}
/* hero */
.hero{position:absolute;left:0;top:0;width:1200px;height:640px;overflow:hidden}
.hero-photo{position:absolute;inset:0;background:linear-gradient(100deg,#3e3c3f 0%,#5a5759 35%,#6e6a6b 55%,#3b3c44 80%,#2e3038 100%)}
.hero-shade{position:absolute;inset:0;background:linear-gradient(180deg,rgba(20,22,30,.55) 0%,rgba(20,22,30,.15) 40%,rgba(20,22,30,.45) 100%)}
.brand{position:absolute;display:flex;align-items:center;gap:10px;color:var(--white);font-size:20px;font-weight:600;letter-spacing:1px;white-space:nowrap}
.brand i{width:16px;height:16px;background:var(--white);display:block}
.nav{position:absolute;left:432px;top:56px;display:flex;gap:21px;font-size:12px;color:var(--white);font-weight:500;white-space:nowrap}
.nav .on{color:var(--blue)}
.phone{position:absolute;display:flex;align-items:center;gap:8px;color:var(--white);font-size:17px;font-weight:500;white-space:nowrap}
.hero-lead{position:absolute;left:160px;top:236px;color:var(--white);font-size:19px;line-height:29px;font-weight:300}
.hero-title{position:absolute;left:160px;top:300px;color:var(--white);font-size:35px;line-height:42px;font-weight:500}
.quick{position:absolute;left:768px;top:155px;width:272px;height:398px;background:var(--white);text-align:center;padding-top:22px}
.quick .pre{font-size:12px;font-weight:500}
.quick h3{color:var(--blue);font-size:19px;font-weight:600;line-height:26px;margin-top:4px}
.field{position:absolute;left:21px;width:230px;height:38px;border:1px solid var(--line);border-radius:19px;font-size:11px;color:var(--muted);text-align:left;padding:11px 16px}
.field.sel::after{content:"";position:absolute;right:16px;top:14px;width:6px;height:6px;border-right:1.5px solid var(--muted);border-bottom:1.5px solid var(--muted);transform:rotate(45deg)}
/* about */
.about-back{position:absolute;left:520px;top:758px;width:40px;height:402px;background:var(--soft)}
.about-back2{position:absolute;left:198px;top:1122px;width:362px;height:38px;background:var(--soft)}
.about-photo{position:absolute;left:160px;top:720px;width:360px;height:402px;background:linear-gradient(135deg,#cfd4d6,#8e9aa0 45%,#5d6a73 80%,#42505a)}
.about h2{position:absolute;left:640px;top:784px;font-size:28px;font-weight:500}
.about .lead{position:absolute;left:640px;top:830px;width:420px;font-size:15px;line-height:23px;color:var(--muted)}
.about .body{position:absolute;left:640px;top:908px;width:420px;font-size:11.5px;line-height:19px;color:var(--muted)}
/* band */
.band{position:absolute;left:0;top:1240px;width:1200px;height:201px;background:var(--blue);color:var(--white);text-align:center}
.band h2{margin-top:52px;font-size:28px;font-weight:300}
.band h2 b{font-weight:600}
.band p{margin-top:6px;font-size:17px;font-weight:300}
.band p b{font-weight:600}
.tab{position:absolute;z-index:3;top:1412px;height:56px;background:var(--white);border-radius:26px 26px 0 0;display:flex;align-items:center;gap:14px;padding:0 8px 8px;font-size:13px;font-weight:500;white-space:nowrap}
.tab span.ic{width:44px;height:44px;border-radius:50%;background:var(--blue);display:flex;align-items:center;justify-content:center;flex:none}
.tab.alt{color:var(--blue)}
/* why */
.why h2{position:absolute;left:79px;top:1530px;font-size:28px;font-weight:500}
.why .lead{position:absolute;left:79px;top:1578px;width:440px;font-size:14px;line-height:24px;color:var(--muted)}
.why ul{position:absolute;left:79px;top:1662px;list-style:none;font-size:11.5px;line-height:27px;color:var(--ink)}
.why li{display:flex;align-items:center;gap:16px}
.why-photo{position:absolute;z-index:1;left:601px;top:1441px;width:599px;height:520px;background:linear-gradient(120deg,#f6d9a0,#e8b883 30%,#c9c9c6 60%,#8f8f92)}
/* features */
.features{position:absolute;left:0;top:1961px;width:1200px;height:454px;background:var(--soft)}
.feat{position:absolute;top:2042px;width:196px;height:215px;text-align:center;padding-top:40px}
.feat.on{background:var(--white);box-shadow:0 8px 24px rgba(0,0,0,.07)}
.feat h4{font-size:14px;font-weight:500;margin-top:10px}
.feat p{font-size:11.5px;line-height:18px;color:var(--muted);margin:8px auto 0;width:150px}
/* testimonial */
.quote{position:absolute;left:0;top:2415px;width:1200px;height:441px;background:var(--blue);color:var(--white);text-align:center}
.quote .mark{position:absolute;left:580px;top:82px;font-size:58px;font-weight:600;line-height:1}
.quote p{position:absolute;left:300px;top:138px;width:600px;font-size:20px;line-height:32px;font-weight:300}
.avatar{position:absolute;left:570px;top:300px;width:60px;height:60px;border-radius:50%;background:linear-gradient(135deg,#f2c77b,#c98b4d);border:3px solid rgba(255,255,255,.6)}
.quote .name{position:absolute;left:0;width:1200px;top:364px;font-size:14px;font-weight:600}
.dot{position:absolute;left:1073px;width:10px;height:10px;border:1.5px solid var(--white);border-radius:50%}
.dot.on{background:var(--white)}
/* enquire */
.enq-photo{position:absolute;left:0;top:2856px;width:1040px;height:460px;background:linear-gradient(180deg,#8d6f86 0%,#d7846a 35%,#f0a25f 55%,#4a4f7a 75%,#1d2448 100%)}
.enq-card{position:absolute;left:599px;top:2921px;width:601px;height:395px;background:var(--white);text-align:center}
.enq-card .pre{margin-top:30px;font-size:14px;font-weight:500}
.enq-card h3{color:var(--blue);font-size:29px;font-weight:600;margin-top:2px}
.in{position:absolute;height:40px;border:1px solid var(--line);border-radius:20px;font-size:11px;color:var(--muted);text-align:left;padding:12px 18px}
/* footer */
.footer{position:absolute;left:0;top:3376px;width:1200px;height:203px;background:var(--footer);color:var(--white)}
.footer .links{position:absolute;left:375px;top:82px;display:flex;gap:22px;font-size:11px}
.footer .copy{position:absolute;left:375px;top:106px;font-size:11px;color:#c9cbd2}
.social{position:absolute;left:1074px;width:14px;height:14px;border-radius:50%;background:var(--white)}
</style>
</head>
<body>

<header class="hero">
  <div class="hero-photo" role="img" aria-label="Dark electric SUV driving along a coastal road at dusk"></div>
  <div class="hero-shade"></div>
  <div class="brand" style="left:72px;top:46px"><i></i>VANTAGE BROKERS</div>
  <nav class="nav"><span class="on">Home</span><span>About</span><span>Services</span><span>Why Us?</span><span>Reviews</span><span>Contact</span></nav>
  <div class="phone" style="left:847px;top:52px">
    <svg width="14" height="14" viewBox="0 0 24 24"><path fill="#fff" d="M6.6 10.8a15 15 0 0 0 6.6 6.6l2.2-2.2c.3-.3.7-.4 1-.2 1.1.4 2.3.6 3.6.6.6 0 1 .4 1 1V20c0 .6-.4 1-1 1A17 17 0 0 1 3 4c0-.6.4-1 1-1h3.5c.6 0 1 .4 1 1 0 1.3.2 2.5.6 3.6.1.3 0 .7-.2 1z"/></svg>
    2800 000 111</div>
  <div class="btn" style="left:993px;top:43px;width:128px;height:43px">Enquire Now</div>

  <p class="hero-lead">We help make sure your next<br>vehicle purchase is the</p>
  <h1 class="hero-title">right car &amp; best deal,<br>hassle free</h1>
  <div class="btn" style="left:160px;top:425px;width:158px;height:40px;font-size:12px">Contact Us Today!</div>

  <form class="quick">
    <div class="pre">We're here to help ...</div>
    <h3>Tell us what you're<br>looking for</h3>
    <div class="field sel" style="top:112px">New / Use</div>
    <div class="field sel" style="top:164px">Select Make</div>
    <div class="field sel" style="top:216px">Model</div>
    <div class="field" style="top:268px">Postcode</div>
    <div class="btn" style="left:72px;top:326px;width:128px;height:40px">Enquire Now!</div>
  </form>
</header>

<section class="about">
  <div class="about-back"></div><div class="about-back2"></div>
  <div class="about-photo" role="img" aria-label="Two men sitting in a car, one adjusting the sunroof"></div>
  <h2>About Vantage Brokers</h2>
  <p class="lead">Lorem ipsum dolor sit amet, consectetur adipiscing elit, sed do eiusmod tempor incididunt ut labore et dolore magna aliqua.</p>
  <p class="body">Ut enim ad minim veniam, quis nostrud exercitation ullamco laboris nisi ut aliquip ex ea commodo consequat. Duis aute irure dolor in reprehenderit in voluptate velit esse cillum dolore eu fugiat nulla pariatur. Excepteur sint occaecat cupidatat non proident, sunt in culpa qui officia deserunt mollit anim id est laborum.</p>
  <div class="btn" style="left:640px;top:1050px;width:112px;height:38px;font-size:12px">About Us</div>
</section>

<section class="band">
  <h2>Better <b>Service</b> • Better <b>Experience</b> • A Better <b>Industry</b></h2>
  <p><b>100%</b> Independent. Australia's owned and operated.</p>
</section>
<div class="tab" style="left:160px;width:293px">
  <span class="ic"><svg width="18" height="18" viewBox="0 0 24 24"><rect x="3" y="3" width="18" height="18" rx="2" fill="none" stroke="#fff" stroke-width="2"/><path d="M7 12l3 3 7-7" fill="none" stroke="#fff" stroke-width="2"/></svg></span>Why Vantage Brokers?</div>
<div class="tab alt" style="left:453px;width:292px">
  <span class="ic"><svg width="18" height="18" viewBox="0 0 24 24"><circle cx="12" cy="8" r="4" fill="#fff"/><path d="M4 21a8 8 0 0 1 16 0z" fill="#fff"/></svg></span>We can Help You!</div>
<div class="tab alt" style="left:745px;width:295px">
  <span class="ic"><svg width="20" height="18" viewBox="0 0 24 24"><path d="M4 16v-4l2-5h12l2 5v4z" fill="none" stroke="#fff" stroke-width="2"/><circle cx="8" cy="16" r="2" fill="#fff"/><circle cx="16" cy="16" r="2" fill="#fff"/></svg></span>Use/New Car Buying</div>

<section class="why">
  <h2>Why Vantage Brokers?</h2>
  <p class="lead">We can help you with new cars, used cars, leasing, import&shy;ing, finance and more. We help make sure your next vehicle purchase is the right car and best deal, hassle free.</p>
  <ul>
    <li><svg width="12" height="10" viewBox="0 0 12 10"><path d="M1 5l3.5 3.5L11 1" fill="none" stroke="#1096dc" stroke-width="2"/></svg>Dislikes the uncertainty as to whether a good price for the new car<br>was achieved</li>
    <li><svg width="12" height="10" viewBox="0 0 12 10"><path d="M1 5l3.5 3.5L11 1" fill="none" stroke="#1096dc" stroke-width="2"/></svg>Hates the phrase "I'll just have to check that with the boss..."</li>
    <li><svg width="12" height="10" viewBox="0 0 12 10"><path d="M1 5l3.5 3.5L11 1" fill="none" stroke="#1096dc" stroke-width="2"/></svg>Would rather not deal with car sales people</li>
    <li><svg width="12" height="10" viewBox="0 0 12 10"><path d="M1 5l3.5 3.5L11 1" fill="none" stroke="#1096dc" stroke-width="2"/></svg>Finds the process of buying a new car to be tiring and stressful</li>
    <li><svg width="12" height="10" viewBox="0 0 12 10"><path d="M1 5l3.5 3.5L11 1" fill="none" stroke="#1096dc" stroke-width="2"/></svg>Want to avoid the dealer tricks</li>
  </ul>
  <div class="btn" style="left:79px;top:1852px;width:128px;height:40px;font-size:12px">Contact Us</div>
  <div class="why-photo" role="img" aria-label="Smiling couple in a car holding up new car keys at sunset"></div>
</section>

<section class="features"></section>
<svg class="abs" style="left:112px;top:2142px" width="16" height="12" viewBox="0 0 16 12"><path d="M15 6H2M6 1L1 6l5 5" fill="none" stroke="#aeb2b8" stroke-width="1.5"/></svg>
<svg class="abs" style="left:1072px;top:2142px" width="16" height="12" viewBox="0 0 16 12"><path d="M1 6h13M10 1l5 5-5 5" fill="none" stroke="#aeb2b8" stroke-width="1.5"/></svg>
<div class="feat" style="left:160px">
  <svg width="48" height="48" viewBox="0 0 48 48"><circle cx="24" cy="27" r="15" fill="none" stroke="#1096dc" stroke-width="2.5"/><path d="M24 18v9l6 4M20 6h8M24 6v6" fill="none" stroke="#1096dc" stroke-width="2.5"/></svg>
  <h4>Save Time</h4><p>Sed ut perspiciatis unde omnis iste natus error sit voluptatem</p></div>
<div class="feat on" style="left:389px">
  <svg width="48" height="48" viewBox="0 0 48 48"><circle cx="26" cy="16" r="11" fill="none" stroke="#1096dc" stroke-width="2.5"/><path d="M26 10v12M22 13h6M6 34h8l8 4h10l8-6" fill="none" stroke="#1096dc" stroke-width="2.5"/></svg>
  <h4>Save Money</h4><p>Sed ut perspiciatis unde omnis iste natus error sit voluptatem</p></div>
<div class="feat" style="left:615px">
  <svg width="48" height="48" viewBox="0 0 48 48"><path d="M6 32v-8l5-10h26l5 10v8z" fill="none" stroke="#1096dc" stroke-width="2.5"/><path d="M6 24h36" stroke="#1096dc" stroke-width="2.5"/><circle cx="14" cy="32" r="4" fill="none" stroke="#1096dc" stroke-width="2.5"/><circle cx="34" cy="32" r="4" fill="none" stroke="#1096dc" stroke-width="2.5"/></svg>
  <h4>Right Car</h4><p>Sed ut perspiciatis unde omnis iste natus error sit voluptatem</p></div>
<div class="feat" style="left:844px">
  <svg width="48" height="48" viewBox="0 0 48 48"><path d="M6 20l10-10 8 6 8-6 10 10-18 18z" fill="none" stroke="#1096dc" stroke-width="2.5"/><path d="M18 24l6 6M22 20l6 6" stroke="#1096dc" stroke-width="2.5"/></svg>
  <h4>Hassle Free</h4><p>Sed ut perspiciatis unde omnis iste natus error sit voluptatem</p></div>
<div class="btn" style="left:528px;top:2298px;width:128px;height:38px;font-size:12px">Our Services</div>

<section class="quote">
  <div class="mark">&#8221;</div>
  <p>Lorem ipsum dolor sit amet, consectetur adipiscing elit, sed do eiusmod tempor incididunt ut labore et dolore magna aliqua. Ut enim ad minim veniam, nostrud exercitation ullamco laboris nisi ...</p>
  <div class="avatar" role="img" aria-label="Client portrait"></div>
  <div class="name">Daniel Hewitt</div>
  <span class="dot on" style="top:188px"></span>
  <span class="dot" style="top:206px"></span>
  <span class="dot" style="top:224px"></span>
  <span class="dot" style="top:242px"></span>
</section>

<section class="enquire">
  <div class="enq-photo" role="img" aria-label="Harbour opera house lit up at sunset over the water"></div>
  <form class="enq-card">
    <div class="pre">We're Here to Help ...</div>
    <h3>Enquire Today!</h3>
    <div class="in" style="left:81px;top:108px;width:212px">Your Name</div>
    <div class="in" style="left:309px;top:108px;width:212px">Email</div>
    <div class="in" style="left:81px;top:162px;width:212px">Phone</div>
    <div class="in" style="left:309px;top:162px;width:212px">Subject</div>
    <div class="in" style="left:81px;top:216px;width:440px;height:82px">Description ...</div>
    <div class="btn" style="left:236px;top:318px;width:130px;height:40px">Enquire Now!</div>
  </form>
</section>

<footer class="footer">
  <div class="brand" style="left:72px;top:80px;font-size:18px"><i></i>VANTAGE BROKERS</div>
  <div class="links"><span>About</span><span>Services</span><span>Why Us?</span><span>Reviews</span><span>Contact</span></div>
  <div class="copy">© 2019 Vantage Brokers. All Rights Reserved.</div>
  <div class="phone" style="left:828px;top:88px;font-size:19px">
    <svg width="15" height="15" viewBox="0 0 24 24"><path fill="#fff" d="M6.6 10.8a15 15 0 0 0 6.6 6.6l2.2-2.2c.3-.3.7-.4 1-.2 1.1.4 2.3.6 3.6.6.6 0 1 .4 1 1V20c0 .6-.4 1-1 1A17 17 0 0 1 3 4c0-.6.4-1 1-1h3.5c.6 0 1 .4 1 1 0 1.3.2 2.5.6 3.6.1.3 0 .7-.2 1z"/></svg>
    2800 000 111</div>
  <span class="social" style="top:56px"></span>
  <span class="social" style="top:86px"></span>
  <span class="social" style="top:116px"></span>
  <span class="social" style="top:146px"></span>
</footer>

</body>
</html>
```